Rural photograpy business card design

I need a business card for my photography business, marisol dovey photography. I would like my logo and pre designed font used on the card. Also my business specialises in photographing rural australia (e.g. shearing sheds, livestock, landscapes, farms), so a rural or country feel to the card would be great. I would like to keep the colours fresh but not too overpowering or juvenile.

Hi,

Could you please add my facebook page to the card - www.snapfolk.net/Marisol/Dovey/Photography.
Thanks,
Marisol.

Reason: I have uploaded two photos I would like either one used on the card.

Target Market(s)

Farmers, country people from their mid twenties onwards

Industry/Entity Type

Business

Contact Information for Business Card

Marisol Dovey Photography. Marisol Pendergast. 1295 Wirrabilla-Kontee Road, Kontee Qld 4871. 0471620394.

Requirements
Must have
• My pre-designed logo and font. Also please add my facebook address - www.snapfolk.net/MarisolDovey/Photography.
Please use one of the photos I have provided.
Should not have
• Peoples faces on the card.

```html
<!DOCTYPE html>
<html lang="en">
<head>
<meta charset="utf-8">
<title>Marisol Dovey Photography – Business Card</title>
<link href="https://fonts.googleapis.com/css2?family=Libre+Baskerville:wght@700&display=swap" rel="stylesheet">
<style>
  :root {
    --sky-deep: #1f5fb3;
    --sky-mid: #4f8fd0;
    --sky-pale: #cfe2ef;
    --sun: #fff6d8;
    --wheat-light: #e9c777;
    --wheat-mid: #c9953c;
    --wheat-dark: #8a5a1c;
    --ink: #141210;
  }
  html, body {
    margin: 0;
    padding: 0;
    width: 1200px;
    height: 693px;
    overflow: hidden;
    background: #ffffff;
  }
  .card {
    position: relative;
    width: 1200px;
    height: 693px;
    overflow: hidden;
    font-family: "Libre Baskerville", Georgia, serif;
    font-weight: 700;
    color: var(--ink);
  }
  .card__photo {
    position: absolute;
    inset: 0;
    background:
      radial-gradient(ellipse 320px 200px at 290px 445px, var(--sun) 0%, rgba(255,246,216,0.6) 40%, rgba(255,246,216,0) 100%),
      linear-gradient(180deg,
        var(--sky-deep) 0%,
        var(--sky-mid) 30%,
        var(--sky-pale) 58%,
        #f3e3b0 64%,
        var(--wheat-light) 70%,
        var(--wheat-mid) 84%,
        var(--wheat-dark) 100%);
  }
  .brand-mark {
    position: absolute;
    left: 515px;
    top: 62px;
    width: 170px;
    height: 170px;
  }
  .brand {
    margin: 0;
    font: inherit;
  }
  .brand__name,
  .brand__trade {
    position: absolute;
    left: 0;
    right: 0;
    text-align: center;
    white-space: nowrap;
  }
  .brand__name {
    top: 283px;
    font-size: 46px;
    line-height: 54px;
    letter-spacing: 0.08em;
  }
  .brand__trade {
    top: 356px;
    font-size: 58px;
    line-height: 72px;
  }
  .contact {
    position: absolute;
    left: 0;
    right: 0;
    top: 446px;
    margin: 0;
    text-align: center;
    font-style: normal;
    font-size: 44px;
    line-height: 53px;
    white-space: nowrap;
  }
  .contact span { display: block; }
  .contact .contact__web {
    margin-top: 4px;
    font-size: 20px;
    line-height: 26px;
  }
</style>
</head>
<body>
  <main class="card">
    <div class="card__photo" role="img" aria-label="Photograph of a golden wheat field under a bright blue sky with the sun low on the horizon"></div>

    <svg class="brand-mark" viewBox="0 0 170 170" aria-hidden="true">
      <circle cx="85" cy="85" r="78" fill="none" stroke="var(--ink)" stroke-width="7"/>
    </svg>

    <h1 class="brand">
      <span class="brand__name">MARISOL DOVEY</span>
      <span class="brand__trade">Photography</span>
    </h1>

    <address class="contact">
      <span class="contact__name">Marisol Pendergast</span>
      <span class="contact__street">1295 Wirrabilla-Kontee Road</span>
      <span class="contact__town">Kontee Qld 4871</span>
      <span class="contact__phone">0471620394</span>
      <span class="contact__web">www.snapfolk.net/MarisolDovey/Photography</span>
    </address>
  </main>
</body>
</html>
```